Flyer für Immobilienfirma
Zielgruppe
Immobilienfirma, klassisches Maklerunternehmen, Zielgruppe in erster Linie Familien.
Aufgabenstellung
Wir benötigen eine klassische Weihnachtskarte für unsere Kunden. Sehr schön wäre es, wenn unser Logo (als Datei anbei) mit auf der Karte erscheint. Es ist eine kreative, moderne, graphische Umsetzung des Themas 'Frohe Weihnachten' erwünscht, bitte eine Fotolösungen mit Weihnachtsbildern. Die Rückseite sollte inhaltlich wie im Beispiel gestaltet sein, die Schrift bitte aber passend zum Design der Vorderseite wählen. Wichtig, da die Karte am Ende über die Druckerei adresstechnisch personalisiert wird, benötigen wir am Ende noch die Schriftart.

```html
<!DOCTYPE html>
<html lang="de">
<head>
<meta charset="utf-8">
<title>Weihnachtskarte – Kaltenbrunn Immobilien</title>
<link href="https://fonts.googleapis.com/css2?family=Montserrat:ital,wght@0,400;0,500;0,600;1,400&display=swap" rel="stylesheet">
<style>
  :root {
    --page-bg: #ffffff;
    --front-stone-light: #d2cfbf;
    --front-stone-dark: #bdb8a4;
    --front-text: #ffffff;
    --back-bg: #ffffff;
    --back-border: #a9a9a9;
    --accent-red: #d7262b;
    --body-grey: #6b6b6b;
    --rule-grey: #d9d9d9;
    --cord: #4a4a4a;
  }
  * { box-sizing: border-box; margin: 0; padding: 0; }
  html, body {
    width: 848px; height: 1200px; overflow: hidden;
    background: var(--page-bg);
    font-family: "Montserrat", Arial, sans-serif;
  }
  .sheet { position: relative; width: 848px; height: 1200px; }
  .symbols { position: absolute; width: 0; height: 0; }

  .brand-mark {
    position: absolute; top: 40px; right: 48px;
    display: flex; align-items: center; gap: 10px;
    font-weight: 600; font-size: 22px; color: var(--accent-red);
  }
  .brand-mark .dot { width: 14px; height: 14px; background: var(--accent-red); border-radius: 50%; }

  /* Cards are built at 536 × 375 and scaled to fit the sheet side by side */
  .card-spread {
    position: absolute; left: 20px; top: 460px;
    width: 1084px; height: 375px;
    transform: scale(0.746); transform-origin: 0 0;
  }
  .card { position: absolute; top: 0; width: 536px; height: 375px; overflow: hidden; }
  .dot-mark { position: absolute; border-radius: 50%; }

  /* Front */
  .card-front {
    left: 0;
    background: linear-gradient(160deg, var(--front-stone-light) 0%, var(--front-stone-dark) 100%);
  }
  .cord { position: absolute; left: 124px; top: 0; width: 1.5px; height: 72px; background: var(--cord); }
  .bulb-illustration {
    position: absolute; left: 64px; top: 68px; width: 124px; height: 212px;
    border-radius: 38% 38% 50% 50% / 22% 22% 36% 36%;
    background: linear-gradient(180deg, #8c8c8c 0%, #b9b6a6 28%, #d9d6ca 62%, #f3f2ee 100%);
  }
  .greeting {
    position: absolute; right: 26px; top: 151px;
    text-align: right; color: var(--front-text);
    font-weight: 500; font-size: 16px; letter-spacing: 3.5px; line-height: 25px;
    text-transform: uppercase;
  }
  .card-front .dot-mark { background: #ffffff; }
  .snowflake { position: absolute; fill: none; stroke-width: 1.6; stroke-linecap: round; }
  .snowflake-front { left: 500px; top: 2px; width: 36px; height: 36px; stroke: #ffffff; }

  /* Back */
  .card-back { left: 548px; background: var(--back-bg); border: 1px solid var(--back-border); }
  .card-back .dot-mark { background: var(--accent-red); }
  .snowflake-back { left: 266px; top: 30px; width: 50px; height: 50px; stroke: var(--accent-red); }
  .salutation {
    position: absolute; left: 22px; top: 28px;
    color: var(--accent-red); font-style: italic; font-size: 13px; line-height: 17px;
  }
  .message {
    position: absolute; left: 22px; top: 77px; width: 240px;
    color: var(--body-grey); font-size: 9.2px; line-height: 14px;
  }
  .message p { margin-bottom: 14px; }
  .message .signature { font-weight: 600; font-size: 10px; margin-top: 0; }
  .divider { position: absolute; left: 293px; top: 138px; width: 1px; height: 146px; background: var(--rule-grey); }
  .address-lines span { position: absolute; left: 305px; width: 208px; height: 1px; background: var(--rule-grey); }
  .footer-brand {
    position: absolute; left: 18px; top: 312px;
    display: flex; align-items: center; gap: 5px;
    font-weight: 600; font-size: 12px; color: var(--accent-red);
  }
  .footer-brand .dot { width: 8px; height: 8px; background: var(--accent-red); border-radius: 50%; }
  .company {
    position: absolute; left: 107px; top: 307px; font-style: normal;
    font-size: 9.4px; line-height: 14px; color: var(--body-grey);
  }
  .company .company-name { color: var(--accent-red); font-weight: 600; }
  .website {
    position: absolute; right: 23px; top: 334px;
    font-size: 9.4px; color: var(--accent-red); font-weight: 500;
  }
</style>
</head>
<body>
<main class="sheet">
  <svg class="symbols" aria-hidden="true">
    <symbol id="snowflake" viewBox="0 0 40 40">
      <path d="M20 3v34M5.3 11.5l29.4 17M5.3 28.5l29.4-17"/>
      <path d="M16 5l4 4 4-4M16 35l4-4 4 4M5 16.5l5.5-1.5-1.5-5.5M35 23.5l-5.5 1.5 1.5 5.5M5 23.5l5.5 1.5-1.5 5.5M35 16.5l-5.5-1.5 1.5-5.5"/>
    </symbol>
  </svg>

  <div class="brand-mark"><span class="dot"></span>Hausglück</div>

  <div class="card-spread">
    <section class="card card-front">
      <span class="cord"></span>
      <div class="bulb-illustration" role="img"
           aria-label="Illustration: hängende Glühbirne als Schneekugel mit Tannenbaum und Holzhütte im Schnee"></div>
      <svg class="snowflake snowflake-front" aria-hidden="true"><use href="#snowflake"/></svg>
      <h1 class="greeting">Frohe Weihnachten<br>und ein glückliches<br>neues Jahr</h1>

      <span class="dot-mark" style="left:26px;top:282px;width:8px;height:8px"></span>
      <span class="dot-mark" style="left:4px;top:298px;width:4px;height:4px"></span>
      <span class="dot-mark" style="left:56px;top:306px;width:4px;height:4px"></span>
      <span class="dot-mark" style="left:114px;top:315px;width:6px;height:6px"></span>
      <span class="dot-mark" style="left:6px;top:334px;width:5px;height:5px"></span>
      <span class="dot-mark" style="left:32px;top:336px;width:8px;height:8px"></span>
      <span class="dot-mark" style="left:100px;top:347px;width:6px;height:6px"></span>
      <span class="dot-mark" style="left:18px;top:357px;width:6px;height:6px"></span>
      <span class="dot-mark" style="left:146px;top:360px;width:8px;height:8px"></span>
      <span class="dot-mark" style="left:92px;top:370px;width:6px;height:6px"></span>
      <span class="dot-mark" style="left:506px;top:360px;width:5px;height:5px"></span>
      <span class="dot-mark" style="left:522px;top:366px;width:7px;height:7px"></span>
    </section>

    <section class="card card-back">
      <p class="salutation">Liebe Kunden, Geschäftspartner<br>und Freunde,</p>
      <svg class="snowflake snowflake-back" aria-hidden="true"><use href="#snowflake"/></svg>

      <div class="message">
        <p>wir möchten uns für Ihr entgegen gebrachtes Vertrauen und die angenehme Zusammen­arbeit bedanken.</p>
        <p>Genießen Sie die Weihnachtszeit mit vielen kleinen Freuden und kommen Sie gesund ins Jahr 2025.</p>
        <p>Aufgrund der aktuellen Notlage vieler Men­schen möchten wir in diesem Jahr erneut mit einer Spende an den Kinderfonds versuche, ein wenig Freude und Zuversicht zu schenken.</p>
        <p class="signature">Ihr Immobilienteam</p>
      </div>

      <div class="divider"></div>
      <div class="address-lines">
        <span style="top:140px"></span><span style="top:176px"></span><span style="top:212px"></span><span style="top:248px"></span><span style="top:284px"></span>
      </div>

      <div class="footer-brand"><span class="dot"></span>Hausglück</div>
      <address class="company">
        <span class="company-name">Kaltenbrunn Immobilien</span><br>
        Lindenweg 12 • 90482 Auenfeld<br>
        09876 543210
      </address>
      <div class="website">www.kaltenbrunn-immobilien.de</div>

      <span class="dot-mark" style="left:424px;top:6px;width:3px;height:3px"></span>
      <span class="dot-mark" style="left:458px;top:11px;width:5px;height:5px"></span>
      <span class="dot-mark" style="left:488px;top:23px;width:4px;height:4px"></span>
      <span class="dot-mark" style="left:496px;top:32px;width:3px;height:3px"></span>
      <span class="dot-mark" style="left:502px;top:48px;width:6px;height:6px"></span>
      <span class="dot-mark" style="left:528px;top:8px;width:8px;height:8px"></span>
      <span class="dot-mark" style="left:515px;top:68px;width:6px;height:6px"></span>
      <span class="dot-mark" style="left:484px;top:60px;width:3px;height:3px"></span>
      <span class="dot-mark" style="left:498px;top:88px;width:3px;height:3px"></span>
      <span class="dot-mark" style="left:531px;top:92px;width:4px;height:4px"></span>
      <span class="dot-mark" style="left:8px;top:361px;width:4px;height:4px"></span>
      <span class="dot-mark" style="left:5px;top:330px;width:3px;height:3px"></span>
      <span class="dot-mark" style="left:41px;top:371px;width:3px;height:3px"></span>
      <span class="dot-mark" style="left:69px;top:370px;width:3px;height:3px"></span>
      <span class="dot-mark" style="left:92px;top:367px;width:4px;height:4px"></span>
    </section>
  </div>
</main>
</body>
</html>
```